Lakeshore Pr Commercial Svcs

I need a business card for my company in Orlando Florida. I provide all property maintenance/repair services both commercial and residential. We also do kitchen and bath remodels, full gut rehab and renovation, and painting. I do not have any suggestions for card layout. I want something that looks great that i can hand out to contractors and home owners to help generate business.

Target Market(s)

contractors, property owners, real estate property managers

Industry/Entity Type

Business

Contact Information for Business Card

Lakeshore Prime Commercial Services, Dale Wexford, 2864 Brambleton Av. Orlando,FL 32806, Owner

```html
<!DOCTYPE html>
<html lang="en">
<head>
<meta charset="utf-8">
<title>Lakeshore Prime Commercial Services – Business Card</title>
<link rel="stylesheet" href="https://fonts.googleapis.com/css2?family=Fira+Sans+Condensed:wght@400;500;600&family=Jost:wght@700&display=swap">
<style>
  :root{
    --page:#e4e4e4;
    --card:#ffffff;
    --navy:#17375a;
    --stone:#a9aaa8;
    --wood:#8d4b27;
    --mosaic:#c9a57b;
    --timber:#c89a68;
    --map-tint:#f1f5f2;
  }
  html,body{margin:0;padding:0;width:1200px;height:1000px;overflow:hidden;background:var(--page);}
  .canvas{position:relative;width:1200px;height:1000px;}
  .card{position:absolute;left:49px;top:166px;width:1098px;height:627px;background:var(--card);
        box-shadow:0 4px 14px rgba(0,0,0,.28);overflow:hidden;}
  .card-art{position:absolute;left:0;top:0;}
  .service-label{position:absolute;color:#fff;font-family:"Fira Sans Condensed",sans-serif;
        font-weight:500;font-size:25px;line-height:1.22;text-align:center;margin:0;}
  .service-label--maintenance{left:180px;top:66px;width:300px;}
  .service-label--trades{left:617px;top:310px;width:300px;line-height:1.75;}
  .brand-name{position:absolute;left:40px;top:390px;width:320px;margin:0;text-align:center;
        color:var(--navy);font-family:"Fira Sans Condensed",sans-serif;text-transform:uppercase;}
  .brand-name__small{display:block;font-size:36px;font-weight:400;line-height:1.1;letter-spacing:.5px;}
  .brand-name__large{display:block;font-size:52px;font-weight:600;line-height:1.05;}
  .brand-name__small + .brand-name__large{margin-top:8px;}
  .contact{position:absolute;right:28px;top:514px;text-align:right;color:var(--navy);margin:0;}
  .contact__owner{display:block;font-family:"Fira Sans Condensed",sans-serif;font-weight:400;
        font-size:26px;letter-spacing:.6px;text-transform:uppercase;}
  .contact__address{display:block;font-family:"Jost",sans-serif;font-weight:700;font-size:25px;
        margin-top:4px;letter-spacing:.3px;}
</style>
</head>
<body>
<div class="canvas">
  <div class="card">
    <svg class="card-art" width="1098" height="627" viewBox="49 166 1098 627">
      <rect role="img" aria-label="Faint outline map of the home state with a star marking the city"
        x="78" y="448" width="418" height="326" rx="6" fill="var(--map-tint)"/>
      <polygon role="img" aria-label="Grey concrete block wall" fill="var(--stone)"
        points="470,166 1147,166 1147,605 1005,515 790,378 605,255"/>
      <g stroke="#fff" stroke-width="10" stroke-linejoin="miter">
        <polygon role="img" aria-label="Dark timber planks" fill="var(--wood)"
          points="40,160 252,160 40,300"/>
        <polygon role="img" aria-label="Wooden mosaic tiles" fill="var(--mosaic)"
          points="40,326 168,248 370,385 40,385"/>
        <polygon class="service-panel" fill="var(--navy)"
          points="180,245 385,105 590,245 385,385"/>
        <polygon role="img" aria-label="Timber planks" fill="var(--wood)"
          points="965,160 1155,160 1155,326"/>
        <polygon role="img" aria-label="Hammer, nails and ruler on lumber" fill="var(--timber)"
          points="400,390 615,255 800,400 600,527"/>
        <polygon class="accent-bar" fill="var(--navy)"
          points="745,345 965,210 988,232 772,365"/>
        <polygon role="img" aria-label="Wooden mosaic tiles" fill="var(--mosaic)"
          points="795,376 982,243 1155,338 1155,430 1010,507"/>
        <polygon fill="var(--stone)" points="1012,520 1155,440 1155,615"/>
        <polygon class="service-panel" fill="var(--navy)"
          points="610,545 815,405 1022,545 815,655"/>
      </g>
    </svg>

    <p class="service-label service-label--maintenance">Property maintenance<br>and repair services</p>
    <p class="service-label service-label--trades">Remodels<br>Renovation<br>Painting</p>

    <h1 class="brand-name">
      <span class="brand-name__small">Lakeshore</span>
      <span class="brand-name__small">Prime</span>
      <span class="brand-name__large">Commercial</span>
      <span class="brand-name__large">Services</span>
    </h1>

    <p class="contact">
      <span class="contact__owner">Dale Wexford - Owner</span>
      <span class="contact__address">2864 Brambleton Av. Orlando, FL 32806</span>
    </p>
  </div>
</div>
</body>
</html>
```